The Wellness Barn Business Card

Info for the front..... (in whichever order and layout looks best)
Carla Penhallow
Physiotherapist
4/37 Upper Creekbank Rd
Tallowbrook
QLD 4712
0462305178
carlapenhallow57@mailbox.example
www.thewellnessbarn.example.au
on the back I would like to be able to write appointments so probably just that heading with lines.
I like a sort of rustic style but mostly professional, colours in naturals, beige, brown, green etc. I dont mind if the logo colour is changed slightly to suit.

```html
<!DOCTYPE html>
<html lang="en">
<head>
<meta charset="utf-8">
<title>The Wellness Barn – Business Cards</title>
<link href="https://fonts.googleapis.com/css2?family=Montserrat:ital,wght@0,400;0,500;0,600;0,700;0,800;1,600&family=Hind:wght@400&display=swap" rel="stylesheet">
<style>
  :root {
    --backdrop: #6f765a;
    --card: #fcfbe8;
    --green: #8ab452;
    --green-deep: #6f9a3a;
    --shadow: rgba(38, 42, 28, 0.55);
  }
  * { box-sizing: border-box; margin: 0; padding: 0; }
  html, body { width: 1200px; height: 1064px; overflow: hidden; }
  body {
    background: var(--backdrop);
    font-family: "Montserrat", sans-serif;
    color: var(--green);
    position: relative;
  }
  .card {
    position: absolute;
    background: var(--card);
    box-shadow: 0 10px 9px -4px var(--shadow);
    overflow: hidden;
  }
  .card--landscape { width: 512px; height: 331px; }
  .card--portrait { width: 331px; height: 511px; }
  .front-h { left: 67px; top: 69px; }
  .back-h { left: 621px; top: 69px; }
  .front-v { left: 248px; top: 483px; }
  .back-v { left: 621px; top: 483px; }

  .abs { position: absolute; }

  .brand {
    position: absolute;
    width: 170px;
    text-align: center;
    font-weight: 800;
    color: var(--green);
    line-height: 0.95;
    text-transform: uppercase;
    letter-spacing: 0.5px;
  }
  .brand__small { display: block; font-size: 20px; }
  .brand__mid { display: block; font-size: 30px; }
  .brand__big { display: block; font-size: 46px; }

  .divider-v { position: absolute; width: 2px; background: var(--green-deep); }
  .rule { position: absolute; height: 1px; background: var(--green-deep); }

  .name { font-size: 21px; letter-spacing: 0.6px; white-space: nowrap; font-weight: 400; }
  .name strong { font-weight: 700; }
  .role { font-family: "Hind", sans-serif; font-size: 16.5px; white-space: nowrap; }
  .address { font-size: 9.5px; font-style: italic; font-weight: 600; line-height: 1.25; }
  .call-use { font-style: italic; font-weight: 600; font-size: 9.5px; }

  .contacts { list-style: none; font-size: 12.5px; line-height: 18px; white-space: nowrap; }
  .contacts li { display: flex; align-items: center; gap: 8px; }
  .contacts svg { width: 12px; height: 12px; flex: none; }
  .contacts--compact { font-size: 11.5px; gap: 0; }
  .contacts--compact li { gap: 7px; }
  .contacts--compact svg { width: 11px; height: 11px; }

  .appt-title { font-size: 23px; font-weight: 600; letter-spacing: 0.5px; white-space: nowrap; }
  .your-name { font-size: 15px; font-weight: 500; white-space: nowrap; }
  .field { position: absolute; display: flex; align-items: flex-end; }
  .field__label { font-size: 12px; text-align: right; white-space: nowrap; }
  .field__line { height: 1px; background: var(--green-deep); margin-left: 7px; margin-bottom: 1px; }
</style>
</head>
<body>

<svg width="0" height="0" style="position:absolute">
  <defs>
    <symbol id="icon-phone" viewBox="0 0 24 24"><path d="M6.6 2.5l3 4-2 2.2a13 13 0 0 0 7.7 7.7l2.2-2 4 3-2 3.3C12 20.5 3.5 12 3.3 4.5z" fill="none" stroke="currentColor" stroke-width="1.6" stroke-linejoin="round"/><path d="M14 3.5a7 7 0 0 1 6.5 6.5M14 7a3.5 3.5 0 0 1 3 3" fill="none" stroke="currentColor" stroke-width="1.4"/></symbol>
    <symbol id="icon-globe" viewBox="0 0 24 24"><circle cx="12" cy="12" r="9.5" fill="none" stroke="currentColor" stroke-width="1.6"/><ellipse cx="12" cy="12" rx="4.3" ry="9.5" fill="none" stroke="currentColor" stroke-width="1.4"/><path d="M2.5 12h19M4 7h16M4 17h16" stroke="currentColor" stroke-width="1.3"/></symbol>
    <symbol id="icon-mail" viewBox="0 0 24 24"><rect x="2" y="5" width="20" height="14" fill="none" stroke="currentColor" stroke-width="1.6"/><path d="M2 5l10 8 10-8M2 19l7.5-7M22 19l-7.5-7" fill="none" stroke="currentColor" stroke-width="1.4"/></symbol>
  </defs>
</svg>

<!-- Front, landscape -->
<section class="card card--landscape front-h">
  <div class="brand" style="left:24px; top:118px;">
    <span class="brand__small">The</span><span class="brand__mid">Wellness</span><span class="brand__big">Barn</span>
  </div>
  <div class="divider-v" style="left:240px; top:13px; height:306px;"></div>
  <p class="abs name" style="right:33px; top:50px;"><strong>CARLA</strong> PENHALLOW</p>
  <p class="abs role" style="right:33px; top:76px;">Physiotherapist</p>
  <div class="rule" style="left:262px; width:217px; top:101px;"></div>
  <p class="abs address" style="right:33px; top:106px; width:230px; text-align:right;">4/37 Upper Creekbank Rd Tallowbrook QLD 4712</p>
  <p class="abs call-use" style="left:264px; top:218px;">CALL USE</p>
  <div class="rule" style="left:264px; width:66px; top:235px;"></div>
  <ul class="abs contacts contacts--compact" style="left:262px; top:241px;">
    <li><svg><use href="#icon-phone"/></svg>0462305178</li>
    <li><svg><use href="#icon-globe"/></svg>www.thewellnessbarn.example.au</li>
    <li><svg><use href="#icon-mail"/></svg>carlapenhallow57@mailbox.example</li>
  </ul>
</section>

<!-- Back, landscape -->
<section class="card card--landscape back-h">
  <p class="abs appt-title" style="left:38px; top:70px;">YOUR APPOINTMENT</p>
  <div class="rule" style="left:38px; width:276px; top:98px;"></div>
  <div class="brand" style="left:321px; top:28px;">
    <span class="brand__small">The</span><span class="brand__mid">Wellness</span><span class="brand__big">Barn</span>
  </div>
  <p class="abs your-name" style="left:38px; top:115px;">Your Name :</p>
  <div class="field" style="left:0; top:200px;"><span class="field__label" style="width:92px;">DAY &nbsp;:</span><span class="field__line" style="width:294px;"></span></div>
  <div class="field" style="left:0; top:236px;"><span class="field__label" style="width:92px;">MONTH &nbsp;:</span><span class="field__line" style="width:294px;"></span></div>
  <div class="field" style="left:0; top:272px;"><span class="field__label" style="width:92px;">YEAR &nbsp;:</span><span class="field__line" style="width:294px;"></span></div>
</section>

<!-- Front, portrait -->
<section class="card card--portrait front-v">
  <div class="brand" style="left:80px; top:50px;">
    <span class="brand__small">The</span><span class="brand__mid">Wellness</span><span class="brand__big">Barn</span>
  </div>
  <p class="abs name" style="left:39px; top:197px;"><strong>CARLA</strong> PENHALLOW</p>
  <p class="abs role" style="left:39px; top:229px;">Physiotherapist</p>
  <div class="rule" style="left:39px; width:254px; top:259px;"></div>
  <p class="abs address" style="left:37px; top:266px; white-space:nowrap;">4/37 Upper Creekbank Rd Tallowbrook QLD 4712</p>
  <p class="abs call-use" style="left:0; width:331px; top:318px; text-align:center; font-size:12.5px;">CALL USE</p>
  <div class="divider-v" style="left:164px; top:349px; height:62px;"></div>
  <ul class="abs contacts" style="left:0; width:331px; top:424px;">
    <li style="justify-content:center;"><svg><use href="#icon-phone"/></svg>0462305178</li>
    <li style="justify-content:center;"><svg><use href="#icon-globe"/></svg>www.thewellnessbarn.example.au</li>
    <li style="justify-content:center;"><svg><use href="#icon-mail"/></svg>carlapenhallow57@mailbox.example</li>
  </ul>
</section>

<!-- Back, portrait -->
<section class="card card--portrait back-v">
  <div class="brand" style="left:81px; top:50px;">
    <span class="brand__small">The</span><span class="brand__mid">Wellness</span><span class="brand__big">Barn</span>
  </div>
  <p class="abs appt-title" style="left:28px; width:276px; top:247px; text-align:center;">YOUR APPOINTMENT</p>
  <div class="rule" style="left:28px; width:276px; top:275px;"></div>
  <p class="abs your-name" style="left:31px; top:289px;">Your Name :</p>
  <div class="field" style="left:0; top:389px;"><span class="field__label" style="width:69px;">DAY &nbsp;:</span><span class="field__line" style="width:241px;"></span></div>
  <div class="field" style="left:0; top:425px;"><span class="field__label" style="width:69px;">MONTH &nbsp;:</span><span class="field__line" style="width:241px;"></span></div>
  <div class="field" style="left:0; top:461px;"><span class="field__label" style="width:69px;">YEAR &nbsp;:</span><span class="field__line" style="width:241px;"></span></div>
</section>

</body>
</html>
```